Brochure 11 x 25.5 Trifold

Brightlane Staffworks, Inc. is a payroll, benefits, and HR administration company. We are in need of a brochure to showcase all of our services. Attached is a one-page information sheet that contains the information we want in the brochure as well as several images. The brochure is a 11 x 25.5 tri-fold (a sample is attached). Please use the colors in the attached logo and design to complement our website brightlanestaff.example.
Target Market(s)
Company executives
Industry/Entity Type
Human Resource Management
Font styles to use
Other font styles liked:
- Avenir LT
Colors
Designer to choose colors to be used in the design.
Look and feel
Each slider illustrates characteristics of the customer's brand and the style your logo design should communicate.

```html
<!DOCTYPE html>
<html lang="en">
<head>
<meta charset="utf-8">
<title>Brightlane Staffworks Trifold</title>
<link rel="stylesheet" href="https://fonts.googleapis.com/css2?family=Roboto+Condensed:wght@400;700&family=Roboto:wght@400;500&family=Mulish:wght@400;600&display=swap">
<style>
  :root{
    --navy:#233a57;
    --green:#7cab3e;
    --ink:#1d2430;
    --white:#ffffff;
    --orange:#e0a21c;
    --olive:#6b6b12;
    --sky:#7db7de;
    --teal:#3f8fa6;
    --red:#c8362a;
    --photo-a:#9aa6ae;
    --photo-b:#6d5a52;
  }
  *{margin:0;padding:0;box-sizing:border-box}
  html,body{width:1200px;height:520px;overflow:hidden;background:var(--white)}
  .brochure{position:relative;width:1200px;height:520px;background:var(--white);font-family:"Roboto",sans-serif;color:var(--ink);overflow:hidden}
  .abs{position:absolute}

  .device-shot{left:29px;top:17px;width:99px;height:208px;border-radius:14px;background:linear-gradient(160deg,#dfe3ea,#5c6876 60%,#3b4653)}

  .intro-title{left:167px;top:32px;font-family:"Roboto Condensed",sans-serif;font-weight:700;font-size:21px;line-height:23.5px;color:var(--green)}
  .intro-copy{left:167px;top:119px;width:194px;font-size:8.8px;line-height:10.2px;text-align:justify}

  .lifecycle-diagram{left:0;top:0}
  .stage-label{font-family:"Mulish",sans-serif;font-size:7.4px;letter-spacing:.2px;line-height:8px}
  .stage-text{font-family:"Mulish",sans-serif;font-size:5.2px;line-height:7.6px;margin-top:3px;color:#333}
  .hiring{left:169px;top:230px;width:82px}.hiring .stage-label{color:var(--orange)}
  .separation{left:75px;top:284px;width:48px}.separation .stage-label{color:var(--red)}
  .onboarding{left:258px;top:291px;width:64px}.onboarding .stage-label{color:var(--olive)}
  .payroll{left:261px;top:371px;width:46px}.payroll .stage-label{color:var(--sky)}
  .management{left:78px;top:383px;width:68px}.management .stage-label{color:var(--navy)}
  .benefits{left:173px;top:424px;width:72px}.benefits .stage-label{color:var(--teal)}
  .lifecycle-core{left:149px;top:339px;width:80px;text-align:center;font-family:"Mulish",sans-serif;font-size:8.6px;line-height:8.6px;color:#333}
  .lifecycle-core b{font-weight:600}

  .corner-name{left:10px;top:482px;font-family:"Mulish",sans-serif;font-weight:600;font-size:14px;color:var(--navy)}

  .brand{display:flex;align-items:center;gap:9px;font-family:"Mulish",sans-serif;font-weight:400;color:var(--navy)}
  .brand-mark{width:14px;height:14px;border-radius:50%;background:var(--green);flex:none}
  .brand-main{left:434px;top:86px;font-size:24px;letter-spacing:.4px}
  .brand-main .brand-mark{width:20px;height:20px}
  .headline{left:434px;top:144px;font-family:"Roboto Condensed",sans-serif;font-weight:700;font-size:30px;line-height:33px;color:var(--green);letter-spacing:.3px}

  .contact{right:427px;top:369px;text-align:right;color:var(--white);font-size:13px;line-height:13px}
  .contact-title{font-family:"Roboto",sans-serif;font-weight:500;font-size:15px;color:var(--green);text-decoration:underline;margin-bottom:17px}
  .contact-row{display:flex;justify-content:flex-end;align-items:center;gap:8px;height:28px}
  .contact-row svg{width:11px;height:11px;fill:var(--green)}

  .team-photo{left:795px;top:0;width:405px;height:404px}
  .brand-side{left:820px;top:376px;font-size:19px}
  .side-rule{left:819px;top:426px;width:42px;height:1px;background:var(--green)}
  .side-lead{left:819px;top:441px;font-family:"Roboto Condensed",sans-serif;font-size:18px;color:var(--ink)}
  .side-title{left:819px;top:464px;font-family:"Roboto Condensed",sans-serif;font-weight:700;font-size:27px;color:var(--navy);letter-spacing:.2px}
  .side-title span{color:var(--green)}
</style>
</head>
<body>
<div class="brochure">

  <!-- Inside panel -->
  <div class="abs device-shot" role="img" aria-label="Smartphone showing the employee portal login screen"></div>
  <h2 class="abs intro-title">From hire to retire,<br>we’ve got you<br>covered</h2>
  <p class="abs intro-copy">Brightlane Staffworks has been delivering quality HR and Payroll services for over 25 years. Our dedicated team of professionals is focused on being the best service provider in the industry. Our goal is to relieve business executives of the challenges of managing a dynamic and growing workforce in today’s regulatory environment and give them the freedom to focus on what drives their business.</p>

  <svg class="abs lifecycle-diagram" width="400" height="520" viewBox="0 0 400 520" aria-hidden="true">
    <defs>
      <marker id="tip-orange" viewBox="0 0 6 6" refX="5" refY="3" markerWidth="6" markerHeight="6" markerUnits="userSpaceOnUse" orient="auto"><path d="M0 0 6 3 0 6" fill="none" stroke="var(--orange)"/></marker>
      <marker id="tip-olive" viewBox="0 0 6 6" refX="5" refY="3" markerWidth="6" markerHeight="6" markerUnits="userSpaceOnUse" orient="auto"><path d="M0 0 6 3 0 6" fill="none" stroke="var(--olive)"/></marker>
      <marker id="tip-sky" viewBox="0 0 6 6" refX="5" refY="3" markerWidth="6" markerHeight="6" markerUnits="userSpaceOnUse" orient="auto"><path d="M0 0 6 3 0 6" fill="none" stroke="var(--sky)"/></marker>
      <marker id="tip-teal" viewBox="0 0 6 6" refX="5" refY="3" markerWidth="6" markerHeight="6" markerUnits="userSpaceOnUse" orient="auto"><path d="M0 0 6 3 0 6" fill="none" stroke="var(--teal)"/></marker>
      <marker id="tip-navy" viewBox="0 0 6 6" refX="5" refY="3" markerWidth="6" markerHeight="6" markerUnits="userSpaceOnUse" orient="auto"><path d="M0 0 6 3 0 6" fill="none" stroke="var(--navy)"/></marker>
      <marker id="tip-red" viewBox="0 0 6 6" refX="5" refY="3" markerWidth="6" markerHeight="6" markerUnits="userSpaceOnUse" orient="auto"><path d="M0 0 6 3 0 6" fill="none" stroke="var(--red)"/></marker>
    </defs>
    <g fill="none" stroke-width="1">
      <path d="M193.5 295.2 A52 52 0 0 1 231.6 317.2" stroke="var(--orange)" marker-end="url(#tip-orange)"/>
      <path d="M236.1 325 A52 52 0 0 1 236.1 369" stroke="var(--olive)" marker-end="url(#tip-olive)"/>
      <path d="M231.6 376.8 A52 52 0 0 1 193.5 398.8" stroke="var(--sky)" marker-end="url(#tip-sky)"/>
      <path d="M184.5 398.8 A52 52 0 0 1 146.4 376.8" stroke="var(--teal)" marker-end="url(#tip-teal)"/>
      <path d="M141.9 369 A52 52 0 0 1 141.9 325" stroke="var(--navy)" marker-end="url(#tip-navy)"/>
      <path d="M146.4 317.2 A52 52 0 0 1 184.5 295.2" stroke="var(--red)" marker-end="url(#tip-red)"/>

      <path d="M189 276 V292" stroke="var(--orange)"/>
      <path d="M251 311 L238 319" stroke="var(--olive)"/>
      <path d="M251 382 L238 374" stroke="var(--sky)"/>
      <path d="M189 402 V418" stroke="var(--teal)"/>
      <path d="M126 382 L139 374" stroke="var(--navy)"/>
      <path d="M126 311 L139 319" stroke="var(--red)"/>
    </g>
  </svg>
  <div class="abs lifecycle-core">EMPLOYEE<br><b>LIFECYCLE</b></div>

  <div class="abs hiring"><div class="stage-label">HIRING</div><div class="stage-text">Integrated cloud-based ATS, Auto post to job boards, applicant management and screening</div></div>
  <div class="abs separation"><div class="stage-label">SEPARATION</div><div class="stage-text">COBRA,<br>Retirement plan assistance, DOL Notining</div></div>
  <div class="abs onboarding"><div class="stage-label">ONBOARDING</div><div class="stage-text">Auto generate notice to new-hire, standard and customized forms and acknowledgements</div></div>
  <div class="abs payroll"><div class="stage-label">PAYROLL</div><div class="stage-text">HRIS, Direct deposits, New Hire Reporting, Employee Portal, Year End Reporting</div></div>
  <div class="abs management"><div class="stage-label">EMPLOYEE<br>MANAGEMENT</div><div class="stage-text">Culture development, discipline, leave management, Workers’ Compensation claims, employee verifications, handbook</div></div>
  <div class="abs benefits"><div class="stage-label">BENEFITS</div><div class="stage-text">Online enrollment, application, benefit reconciliations, eligibility tracking notifications, retirement plan</div></div>

  <div class="abs corner-name">Brightlane</div>

  <!-- Back panel -->
  <svg class="abs" style="left:0;top:0" width="1200" height="520" viewBox="0 0 1200 520" aria-hidden="true">
    <polygon points="231,520 390,402 795,287 795,520" fill="var(--green)"/>
    <polygon points="240,520 396,410 795,296 795,520" fill="var(--navy)"/>
  </svg>

  <div class="abs brand brand-main"><span class="brand-mark"></span>BRIGHTLANE STAFFWORKS</div>
  <h1 class="abs headline">SAVE TIME AND STAY<br>FOCUSED ON RUNNING<br>YOUR BUSINESS</h1>

  <div class="abs contact">
    <div class="contact-title">Contact Us:</div>
    <div class="contact-row"><svg viewBox="0 0 12 12"><path d="M6 0a4 4 0 0 0-4 4c0 3 4 8 4 8s4-5 4-8a4 4 0 0 0-4-4zm0 5.5A1.5 1.5 0 1 1 6 2.5a1.5 1.5 0 0 1 0 3z"/></svg>412 Orchard Row • Maple Falls, OR • 97000</div>
    <div class="contact-row"><svg viewBox="0 0 12 12"><path d="M2.5 0 4.5 3 3.3 4.6a7 7 0 0 0 4.1 4.1L9 7.5l3 2-1.5 2.3C5 12 0 7 .2 1.5z"/></svg>555-013-4200</div>
    <div class="contact-row"><svg viewBox="0 0 12 12"><path d="M0 2h12v8H0zm1 1 5 4 5-4z" fill-rule="evenodd"/></svg>info@brightlanestaff.example</div>
    <div class="contact-row"><svg viewBox="0 0 12 12"><circle cx="6" cy="6" r="5.5"/><path d="M.5 6h11M6 .5v11" stroke="var(--navy)" stroke-width=".8"/></svg>www.brightlanestaff.example</div>
  </div>

  <!-- Cover panel -->
  <svg class="abs team-photo" viewBox="0 0 405 404" role="img" aria-label="Photo of a smiling team of colleagues working together at a laptop in a bright office">
    <defs><linearGradient id="photoTone" x1="0" y1="0" x2="1" y2="1"><stop offset="0" stop-color="var(--photo-a)"/><stop offset="1" stop-color="var(--photo-b)"/></linearGradient></defs>
    <polygon points="0,0 405,0 405,404 0,294" fill="url(#photoTone)"/>
    <polygon points="0,302 405,412 405,404 0,294" fill="var(--navy)"/>
  </svg>

  <div class="abs brand brand-side"><span class="brand-mark"></span>BRIGHTLANE STAFFWORKS</div>
  <div class="abs side-rule"></div>
  <div class="abs side-lead">Your single-source solution for the</div>
  <div class="abs side-title">ENTIRE <span>EMPLOYEE LIFECYCLE</span></div>
</div>
</body>
</html>
```